UK Leading HighTech Tooling distributor letterhead

We are one of the UK's leading Engineering Tooling distributers, we are launching our great new catalogue in May and want a red-hot eye catching letterhead to accompany the catalogue.

We want customers who see it to think high quality and premium.

We will roll out the successful style of design accross our other marketing goods (bus cards, website, emails etc) so the winning design will gain more work as a result.

Finally - we are in a rush so please submit quickly your best designs!

Target Market(s)

Precision engineers, senior buyers and managing directors.

Industry/Entity Type

Marketing

Requirements
Must have
• It must feature the Brevix logo as the MAIN logo.
It must have a tag line of 'Complete Tooling Solutions' somewhere on the page.
It should feature our 6 supplier logo's as sub logo's

Contact details:
tel 01632 457203
fax 01632 457204
web brevixparts.example.uk
email sales@brevix.example.net
address : Brevix Ltd, Harlow Yard, Marsh Lane, Dewsbury, West Yorkshire, ZX98 4QP, United Kingdom
Company registration 7481530
Vat no. 518 2407 61
Nice to have
• Bring our logo alive

I have attached an old version of our letterhead so you can see details - please make it much better!

```html
<!DOCTYPE html>
<html lang="en">
<head>
<meta charset="utf-8">
<title>Brevix Letterhead</title>
<link href="https://fonts.googleapis.com/css2?family=PT+Sans:wght@400;700&family=Source+Sans+3:wght@300;400;600&display=swap" rel="stylesheet">
<style>
  :root {
    --backdrop: #1c1c1c;
    --paper: #ffffff;
    --brand-blue: #2a9fd6;
    --deep-blue: #1b72b8;
    --ink: #1f1f1f;
    --muted: #5c5c5c;
    --partner-ink: #1d2a5a;
  }
  * { box-sizing: border-box; margin: 0; padding: 0; }
  html, body {
    width: 1042px; height: 1200px; overflow: hidden;
    background: var(--backdrop);
  }
  .letterhead {
    position: absolute; left: 57px; top: 0;
    width: 928px; height: 1200px;
    background: var(--paper);
    overflow: hidden;
  }
  .brand {
    position: absolute; left: 71px; top: 96px;
    display: flex; align-items: center; gap: 14px;
  }
  .brand-dot {
    width: 44px; height: 44px; border-radius: 50%;
    background: var(--brand-blue);
  }
  .brand-name {
    font-family: "Source Sans 3", sans-serif;
    font-weight: 600; font-size: 52px; line-height: 1;
    color: var(--brand-blue);
  }
  .contact {
    position: absolute; right: 31px; top: 50px;
    text-align: right;
    font-family: "Source Sans 3", sans-serif;
    font-weight: 300; font-size: 14px; line-height: 19.8px;
    color: var(--muted);
  }
  .contact .company { font-weight: 600; color: var(--brand-blue); font-size: 14.5px; }
  .contact .label { font-weight: 400; color: var(--brand-blue); }
  .contact .gap { margin-left: 10px; }
  .letter-body {
    position: absolute; left: 117px; top: 306px; width: 677px;
    font-family: "PT Sans", sans-serif;
    font-size: 14.6px; line-height: 18px;
    color: var(--ink);
    text-align: justify; hyphens: auto;
  }
  .letter-body p + p { margin-top: 18px; }
  .signature {
    position: absolute; left: 127px; top: 912px;
    width: 143px; height: 108px;
    background: linear-gradient(135deg, #f2f2f2, #e4e4e4);
  }
  .partners {
    position: absolute; left: 23px; top: 1118px; width: 690px;
    display: flex; justify-content: space-between; align-items: center;
    font-family: "PT Sans", sans-serif; font-weight: 700;
    font-size: 19px; color: var(--partner-ink);
  }
  .footer-band {
    position: absolute; left: 0; bottom: 0; width: 100%; height: 40px;
    background: linear-gradient(90deg, var(--deep-blue) 0%, #55aede 32%, var(--deep-blue) 100%);
  }
  .tagline {
    position: absolute; right: 221px; bottom: 7px;
    font-family: "Source Sans 3", sans-serif; font-weight: 400;
    font-size: 21px; color: var(--paper);
  }
  .footer-brand {
    position: absolute; left: 740px; top: 1115px;
    font-family: "Source Sans 3", sans-serif; font-weight: 600;
    font-size: 40px; line-height: 1; color: var(--brand-blue);
  }
</style>
</head>
<body>
<main class="letterhead">
  <div class="brand">
    <span class="brand-dot"></span>
    <span class="brand-name">Brevix</span>
  </div>

  <address class="contact" style="font-style:normal">
    <div class="company">Brevix Limited</div>
    <div>Harlow Yard, Marsh Lane, Dewsbury,</div>
    <div>West Yorkshire, ZX98 4QP, United Kingdom,</div>
    <div><span class="label">Company registration</span> 7481530</div>
    <div><span class="label">Vat No.</span> 518 2407 61</div>
    <div><span class="label">phone.</span> 01632 457203 <span class="label gap">fax.</span> 01632 457204</div>
    <div><span class="label">email.</span> sales@brevix.example.net <span class="label gap">web.</span> brevixparts.example.uk</div>
  </address>

  <section class="letter-body">
    <p>Lorem ipsum dolor sit amet, consectetuer adipiscing elit. Pellentesque tristique elementum sem. Quisque eget erat ac lectus sodales faucibus. Nam commodo est. Cras consequat faucibus velit. Nam ac magna. Sed et ligula. Nam volutpat, elit ac facilisis tempor, neque augue euismod leo, sit amet molestie sem est eu libero. Nulla facilisi. Pellentesque sit amet odio. Curabitur a leo consectetuer leo blandit porttitor. Pellentesque velit quam, gravida at, pharetra eu, convallis non, sem. Aenean tempor nibh at purus. Pellentesque porta. Suspendisse congue, lacus sit amet imperdiet imperdiet, urna massa rutrum urna, id elementum tellus diam quis risus.</p>
    <p>In dui turpis, varius vitae, tincidunt id, consequat ut, leo. Donec tincidunt tristique odio. Nulla erat felis, euismod nec, fringilla non, aliquet et, magna. Nulla at magna quis nisi pretium vehicula. Pellentesque habitant morbi tristique senectus et netus et malesuada fames ac turpis egestas. Class aptent taciti sociosqu ad litora torquent per conubia nostra, per inceptos himenaeos. In vel quam. Phasellus varius convallis purus. In non turpis. Nam sed risus. Etiam non neque at nisl gravida porttitor. Donec leo dolor, feugiat ut, pharetra et, porttitor a, metus. Suspendisse laoreet magna vel elit. Ut est augue, fermentum ac, molestie at, vestibulum et, urna.</p>
    <p>Nunc purus. Cras auctor. In ornare neque id ipsum. Nulla tincidunt, diam sit amet viverra euismod, sapien augue fringilla neque, at pellentesque felis tortor vel enim. Etiam dignissim. Sed a tortor vel nisl euismod ultricies. Donec molestie congue lectus. Integer sed turpis a tortor imperdiet consequat. Maecenas molestie placerat urna. Sed pede enim, sollicitudin nec, pretium nec, sollicitudin a, felis. In hac habitasse platea dictumst. Nam facilisis, tellus non scelerisque placerat, turpis turpis semper ante, euismod imperdiet augue nisi et neque. Vivamus tincidunt.</p>
    <p>Nulla lobortis ultricies nulla. Pellentesque purus mi, consequat quis, hendrerit sed, imperdiet non, eros. Nullam urna est, vehicula nec, cursus nec, dignissim sit amet, risus. Duis molestie, tellus sit amet laoreet ullamcorper, urna nisi fringilla ante, at rhoncus justo dolor vel dui. Nam hendrerit luctus lorem. Aenean tempor, metus vel posuere gravida, arcu nunc imperdiet tellus, ut blandit sem magna a turpis. Vivamus in neque. Lorem ipsum dolor sit amet, consectetuer adipiscing elit. Duis tristique tortor id nisl feugiat posuere. Maecenas posuere nisi ac risus. Nunc hendrerit. Praesent porta tempus ligula. Morbi in leo. Curabitur sapien nulla, cursus eget, faucibus in, porttitor et, odio. Praesent sed justo sed arcu commodo feugiat. Duis facilisis nulla ut eros. Cras libero. Donec mollis consectetuer metus. Praesent odio.</p>
  </section>

  <div class="signature" role="img" aria-label="Handwritten signature of the sender"></div>

  <div class="partners">
    <span class="partner">Tornex</span>
    <span class="partner">Valdan Inc.</span>
    <span class="partner">Merlotti</span>
    <span class="partner">Halvern</span>
    <span class="partner">Orvik Inc.</span>
    <span class="partner">Stelwick</span>
  </div>

  <div class="footer-brand">Brevix</div>
  <div class="footer-band"></div>
  <div class="tagline">Complete Tooling Solutions</div>
</main>
</body>
</html>
```